Morvane Locks price sheet/brochure

So I'm looking to create a pricing sheet/brochure for my hair company. The company name is "Morvane Locks" and we specialize in providing Peruvian, Brazilian and Indian weave hair. I created a logo some time ago that I'd like to use if possible. If not, I'll need to create a logo as well!

8.5 x 11....not sure how many pages are needed to properly display all pricing, but I'd like the pricing to be at a size that makes it easy for the client to read. Open A-3

Target Market(s)

Hair stylist as well as their clients. Looking to establish business in Africa as well!

Industry/Entity Type

Hair And Beauty

Font styles to use
Serif

Colors
e34298

Requirements
Must have
• Price sheet/brochure must be easy to read and give potential client all the pertinent information needed regarding our hair! Also want the brochure to present style and pride in the excellent quality hair the "Morvane Locks"! 😀
• Morvane Locks
• Base price for all hair textures. Pricing will increase depending on wave pattern.
• Peruvian & Brazilian Virgin Hair
• 4 bundle deals
• 10, 12, 14, 16 - $405
• 12, 14, 16, 18 - $434
• 14, 16, 18, 20 - $467
• 16, 18, 20, 22 - $504
• 18, 20, 22, 24 - $539
• 20, 22, 24, 26 - $576
• 22, 24, 26, 28 - $621
• 24, 26, 28, 30 - $660
• 26, 28, 30, 32 - $693
• 28, 30, 32, 34 - $728
• 30, 32, 34, 36 - $760
• 32, 34, 36, 38 - $799
• 3 bundle deals
• 10, 12, 14 - $281
• 12, 14, 16 - $333
• 14, 16, 18 - $358
• 16, 18, 20 - $385
• 18, 20, 22 - $410
• 20, 22, 24 - $432
• 22, 24, 26 - $471
• 24, 26, 28 - $500
• 26, 28, 30 - $533
• 28, 30, 32 - $560
• 30, 32, 34 - $589
• 32, 34, 36 - $608
• 34, 36, 38 - $635
• 2 Bundles
• 2 Bundles 10 - $203
• 2 Bundles 12 - $235
• 2 Bundles 14 - $251
• 2 Bundles 16 - $272
• 2 Bundles 18 - $285
• 2 Bundles 20 - $302
• 2 Bundles 22 - $346
• 2 Bundles 24 - $345
• 2 Bundles 26 - $357
• 2 Bundles 28 - $384
• 2 Bundles 30 - $418
• 2 Bundles 32 - $429
• 2 Bundles 34 - $440
• 2 Bundles 36 - $476
• 2 Bundles 38 - $502
• 1 Bundle
• 1 Bundle 10 - $97
• 1 Bundle 12 - $110
• 1 Bundle 14 - $116
• 1 Bundle 16 - $126
• 1 Bundle 18 - $134
• 1 Bundle 20 - $141
• 1 Bundle 22 - $154
• 1 Bundle 24 - $167
• 1 Bundle 26 - $172
• 1 Bundle 28 - $185
• 1 Bundle 30 - $192
• 1 Bundle 32 - $197
• 1 Bundle 34 - $205
• 1 Bundle 36 - $215
• 1 Bundle 38 - $230
• -----------------------------------------------------------------------------
• Indian Virgin Hair
• 4 bundle deals
• 10, 12, 14, 16 - $293
• 12, 14, 16, 18 - $314
• 14, 16, 18, 20 - $325
• 16, 18, 20, 22 - $348
• 18, 20, 22, 24 - $367
• 20, 22, 24, 26 - $386
• 22, 24, 26, 28 - $407
• 24, 26, 28, 30 - $425
• 26, 28, 30, 32 - $444
• 28, 30, 32, 34 - $461
• 30, 32, 34, 36 - $477
• 32, 34, 36, 38 - $495
• 3 bundle deals
• 10, 12, 14 - $223
• 12, 14, 16 - $239
• 14, 16, 18 - $252
• 16, 18, 20 - $264
• 18, 20, 22 - $278
• 20, 22, 24 - $293
• 22, 24, 26 - $308
• 24, 26, 28 - $322
• 26, 28, 30 - $337
• 28, 30, 32 - $350
• 30, 32, 34 - $262
• 32, 34, 36 - $375
• 34, 36, 38 - $390
• 2 Bundles
• 2 Bundles 10 - $74
• 2 Bundles 12 - $90
• 2 Bundles 14 - $98
• 2 Bundles 16 - $107
• 2 Bundles 18 - $115
• 2 Bundles 20 - $123
• 2 Bundles 22 - $135
• 2 Bundles 24 - $143
• 2 Bundles 26 - $154
• 2 Bundles 28 - $164
• 2 Bundles 30 - $172
• 2 Bundles 32 - $180
• 2 Bundles 34 - $189
• 2 Bundles 36 - $197
• 2 Bundles 38 - $207
• 1 Bundle
• 1 Bundle 10 - $80
• 1 Bundle 12 - $88
• 1 Bundle 14 - $93
• 1 Bundle 16 - $98
• 1 Bundle 18 - $102
• 1 Bundle 20 - $109
• 1 Bundle 22 - $115
• 1 Bundle 24 - $122
• 1 Bundle 26 - $130
• 1 Bundle 28 - $137
• 1 Bundle 30 - $144
• 1 Bundle 32 - $156
• 1 Bundle 34 - $163
• 1 Bundle 36 - $175
• 1 Bundle 38 - $190
• Hair Care
• It's very important to take good care of your hair to keep using long time, below are some brief introduction
• IMPORTANT: Treat 100% human hair extensions gently.
• 1. Wash and condition hair regularly, at maximum of 3 times a week. This will keep the moisture in from shampooing while at the same time not drying them out from over shampooing.
• 2. Combing hair gently before washing. Do not rub or twist hair.
• 3. Add mild shampoo to cool water or warm water about 35℃ (Please do not use hot water) and swish hair till clean. Rinse thoroughly.
• 4. Blot out excess water with towel and allow hair to dry naturally. Do not expose to sun
• 5. Comb curly hair gently with your fingers from end to top. Do not brush
• 6. Hair may be tangled if general care directions are not followed properly.
• Important Note:
• Brush the end of hair first, then the middle, and the top at last. DO NOT brush directly from the top and pull hard, it will break the hair. Regular care will keep the hair in good condition and avoid tangle problem, improper dyeing or other chemical process will damage the hair and cause tangle and shedding problem. Please wash the hair with warm water before proceeding dyeing.
• Details of Hair Extension Maintenance Tips
• Straight Hair:
• Maintenance
• • Shampoo at least once a week.
• • Use a shampoo no higher than pH 7.
• • Dilute one ounce of shampoo in a bowl or jug with a pint of warm water.
• • Sponge the shampoo into the hair.
• • Do not massage.
• • Rinse thoroughly.
• • Apply conditioner and comb hair, starting with the ends working your way up to your scalp.
• • Rinse thoroughly.
• • Let air-dry.
• Daily
• • Brush or comb through to style.
• • Use styling aids, such as mouse, gel, and hairspray in moderation (preferably alcohol free products).
• Sleep
• • Before going to bed, braid your hair into one loose large braid at the back of the neck.
• • After waking up, undo braid and comb through beginning at the ends and working your way up to roots.
• Natural Body Wave Hair
• Maintenance
• • Do not massage.
• • Rinse thoroughly.
• • Rinse thoroughly.
• • Let air-dry.
• • Style as desired.
• • For extra wave, hair can be set in rollers.
• Daily
• Sleep
• • After waking up, undo braid.
• • Dampen hair with a water bottle.
• • Comb through beginning at the ends and working your way up to roots.
• • Let hair air-dry.
• • Style as desired.
• For extra wave, hair can be set in rollers.
• Permed Curly and Natural Curly Hair
• Maintenance
• • Do not use oil products on permed hair, it can cause matting.
• • Do not brush or comb hair when dry, it will cause frizz and the ends may tangle.
• • Do not massage.
• • Rinse thoroughly.
• • Rinse thoroughly.
• • Scrunch up hair gently to reform curl.
• • Let air-dry.
• • Style as desired.
• Daily
• Sleep
• • Let hair air-dry.
• • Style as desired.
• Specific Conditions
• Static:
• • In colder months, you may experience some static. The best way to deal with this is to dampen your hands with water, and rub hand together so they are warm. Run the palms of your hands over your hair, without actually touching your hair. This process should help control the static.
• Swimming:
• It is not recommended that you swim with extension hair. However if you do the following precautions are recommended.
• • Never wear a swimming cap or anything that covers your hair, the friction may cause matting.
• • Before swimming comb out tangles.
• • Braid hair into one braid at back of neck.
• • Try to keep head above water.
• • Do not swim under water.
• • No diving.
• • After swimming keep head out of shower.
• • Immediately after showering undo braid, comb hair and let air-dry.
• • Follow with appropriate shampooing and conditioning as needed.
• Sauna:
• • The water of the sauna will penetrate the hair and wet it.
• • Do not wrap hair in towel, which will compress it.
• • After sauna keep head out of shower.
• Sunbathing:
• • After sunbathing do not unbraid until hair has cooled down.
• • After hair cools, undo braid, comb hair.
• Miscellaneous Tips:
• • Although the extension hair is real, it is not receiving nutrients from the scalp like your own hair. Heat is your hair extensions biggest enemy. The more you use on it, the shorter the life span of your hair. We cannot guarantee that the hair will remain silky if you use the blow dry, flat iron, or curling iron often.
• • When you sleep, we highly recommend that you braid, wrap or ponytail your hair together to prevent tangling. This will save time that would be spent untangling the hair the next morning.
• • When washing the hair, always wash it going in a downward motion. Use your fingers in a horizontal motion between wefts to clean your scalp. When rinsing, do the same to be sure that all the shampoo and conditioner residues are washed out.
• Sent from my Vorna
Nice to have
• Ditto....tried to upload logo but it was to big. Please advise!
Should not have
• Ditto....

```html
<!DOCTYPE html>
<html lang="en">
<head>
<meta charset="utf-8">
<title>Morvane Locks — Price Sheet, Pages 2–3</title>
<link href="https://fonts.googleapis.com/css2?family=Tinos:wght@400;700&family=Arimo:wght@400&display=swap" rel="stylesheet">
<style>
  :root{
    --brand-pink:#e34298;
    --bar-pink:#e8288f;
    --ink:#2b2b2b;
    --paper:#ffffff;
    --frame:#9a9a9a;
    --magenta-core:#e0168a;
    --magenta-mid:#a8135f;
    --magenta-edge:#4e0d2a;
    --ring-pink:#e8288f;
    --ring-green:#8dc63f;
    --ring-white:#ffffff;
  }
  *{margin:0;padding:0;box-sizing:border-box}
  html,body{width:1200px;height:945px;overflow:hidden;background:var(--paper)}
  body{position:relative;font-family:"Tinos","Times New Roman",serif;color:var(--ink)}
  .canvas{position:absolute;inset:0;border:1px solid #555}

  /* ---------- Page 2: price list ---------- */
  .page{position:absolute;top:35px;height:853px}
  .page--prices{left:22px;width:578px;background:var(--paper);border:1px solid var(--frame)}
  .page--care{left:600px;width:577px;
    background:radial-gradient(ellipse 70% 62% at 52% 52%,var(--magenta-core) 0%,var(--magenta-mid) 55%,var(--magenta-edge) 100%);}

  .intro{position:absolute;left:51px;top:48px;color:var(--brand-pink);font-weight:700;font-size:21px;line-height:32px}

  .origin-bar{position:absolute;top:113px;height:24px;background:var(--bar-pink);color:#fff;
    font-weight:700;font-size:12.5px;line-height:24px;text-align:center}
  .origin-bar::after{content:"";position:absolute;top:24px;left:50%;margin-left:-6px;
    border-left:6px solid transparent;border-right:6px solid transparent;border-top:7px solid var(--bar-pink)}
  .origin-bar--pb{left:44px;width:237px}
  .origin-bar--in{left:301px;width:226px}
  .column-divider{position:absolute;left:288px;top:113px}

  .price-col{position:absolute;list-style:none}
  .price-col h3{font-size:16px;font-weight:700;color:var(--brand-pink);line-height:20px;margin-bottom:6px}
  .price-col li{font-size:11.2px;font-weight:700;line-height:21.2px;white-space:nowrap}
  .col-a{left:51px}.col-b{left:170px}.col-c{left:305px}.col-d{left:435px}
  .row-single{top:152px}
  .row-deals{top:512px}

  /* ---------- Page 3: hair care ---------- */
  .care-copy{position:absolute;left:51px;width:476px;color:#fff;font-size:11.4px;line-height:14.3px;letter-spacing:-.1px}
  .care-copy h2{font-size:14px;font-weight:700;line-height:16px}
  .care-copy h3{font-size:11.6px;font-weight:700;line-height:14.3px}
  .care-copy p{text-align:justify}
  .care-copy ul{list-style:none}
  .care-copy li{padding-left:9px;text-indent:-9px}
  .care-copy li::before{content:"• "}
  .care-intro{top:43px}
  .care-note{top:244px}
  .care-tips{top:342px}
  .care-daily{top:536px;width:220px}
  .care-sleep{top:630px;width:310px}

  .swatch{position:absolute;border-radius:50%}
  .swatch__fill{position:absolute;inset:7px;border-radius:50%;
    background:radial-gradient(circle at 50% 45%,#4a4a4a 0%,#1b1b1b 45%,#d9d9d9 80%,#f4f4f4 100%)}
  .swatch--loose{left:272px;top:517px;width:126px;height:126px;background:var(--ring-white);border:3px solid var(--ring-pink)}
  .swatch--body{left:432px;top:525px;width:128px;height:128px;background:var(--ring-pink)}
  .swatch--deep{left:166px;top:703px;width:124px;height:124px;background:var(--ring-green)}
  .swatch--straight{left:356px;top:685px;width:132px;height:132px;background:var(--ring-green)}

  .page-label{position:absolute;top:890px;font-family:"Arimo",Arial,sans-serif;font-size:30px;color:#111}
  .page-label--2{left:234px}
  .page-label--3{left:808px}
</style>
</head>
<body>
<div class="canvas">

  <section class="page page--prices">
    <p class="intro">Base price for all hair textures.<br>Pricing will increase depending on wave pattern.</p>

    <div class="origin-bar origin-bar--pb">Peruvian &amp; Brazilian Virgin Hair</div>
    <div class="origin-bar origin-bar--in">Indian Virgin Hair</div>
    <svg class="column-divider" width="4" height="560" viewBox="0 0 4 560" aria-hidden="true">
      <path d="M0 0 H4 L2.2 560 H1.8 Z" fill="var(--bar-pink)"/>
    </svg>

    <ul class="price-col col-a row-single"><h3>1 Bundle</h3>
      <li>1 Bundle 10 - $97</li><li>1 Bundle 12 - $110</li><li>1 Bundle 14 - $116</li><li>1 Bundle 16 - $126</li><li>1 Bundle 18 - $134</li><li>1 Bundle 20 - $141</li><li>1 Bundle 22 - $154</li><li>1 Bundle 24 - $167</li><li>1 Bundle 26 - $172</li><li>1 Bundle 28 - $185</li><li>1 Bundle 30 - $192</li><li>1 Bundle 32 - $197</li><li>1 Bundle 34 - $205</li><li>1 Bundle 36 - $215</li><li>1 Bundle 38 - $230</li>
    </ul>
    <ul class="price-col col-b row-single"><h3>2 Bundles</h3>
      <li>2 Bundles 10 - $203</li><li>2 Bundles 12 - $235</li><li>2 Bundles 14 - $251</li><li>2 Bundles 16 - $272</li><li>2 Bundles 18 - $285</li><li>2 Bundles 20 - $302</li><li>2 Bundles 22 - $346</li><li>2 Bundles 24 - $345</li><li>2 Bundles 26 - $357</li><li>2 Bundles 28 - $384</li><li>2 Bundles 30 - $418</li><li>2 Bundles 32 - $429</li><li>2 Bundles 34 - $440</li><li>2 Bundles 36 - $476</li><li>2 Bundles 38 - $502</li>
    </ul>
    <ul class="price-col col-c row-single"><h3>1 Bundle</h3>
      <li>1 Bundle 10 - $80</li><li>1 Bundle 12 - $88</li><li>1 Bundle 14 - $93</li><li>1 Bundle 16 - $98</li><li>1 Bundle 18 - $102</li><li>1 Bundle 20 - $109</li><li>1 Bundle 22 - $115</li><li>1 Bundle 24 - $122</li><li>1 Bundle 26 - $130</li><li>1 Bundle 28 - $137</li><li>1 Bundle 30 - $144</li><li>1 Bundle 32 - $156</li><li>1 Bundle 34 - $163</li><li>1 Bundle 36 - $175</li><li>1 Bundle 38 - $190</li>
    </ul>
    <ul class="price-col col-d row-single"><h3>2 Bundles</h3>
      <li>2 Bundles 10 - $74</li><li>2 Bundles 12 - $90</li><li>2 Bundles 14 - $98</li><li>2 Bundles 16 - $107</li><li>2 Bundles 18 - $115</li><li>2 Bundles 20 - $123</li><li>2 Bundles 22 - $135</li><li>2 Bundles 24 - $143</li><li>2 Bundles 26 - $154</li><li>2 Bundles 28 - $164</li><li>2 Bundles 30 - $172</li><li>2 Bundles 32 - $180</li><li>2 Bundles 34 - $189</li><li>2 Bundles 36 - $197</li><li>2 Bundles 38 - $207</li>
    </ul>

    <ul class="price-col col-a row-deals"><h3>3 bundle deals</h3>
      <li>10, 12, 14 - $281</li><li>12, 14, 16 - $333</li><li>14, 16, 18 - $358</li><li>16, 18, 20 - $385</li><li>18, 20, 22 - $410</li><li>20, 22, 24 - $432</li><li>22, 24, 26 - $471</li><li>24, 26, 28 - $500</li><li>26, 28, 30 - $533</li><li>28, 30, 32 - $560</li><li>30, 32, 34 - $589</li><li>32, 34, 36 - $608</li><li>34, 36, 38 - $635</li>
    </ul>
    <ul class="price-col col-b row-deals"><h3>4 bundle deals</h3>
      <li>10, 12, 14, 16 - $405</li><li>12, 14, 16, 18 - $434</li><li>14, 16, 18, 20 - $467</li><li>16, 18, 20, 22 - $504</li><li>18, 20, 22, 24 - $539</li><li>20, 22, 24, 26 - $576</li><li>22, 24, 26, 28 - $621</li><li>24, 26, 28, 30 - $660</li><li>26, 28, 30, 32 - $693</li><li>28, 30, 32, 34 - $728</li><li>30, 32, 34, 36 - $760</li><li>32, 34, 36, 38 - $799</li>
    </ul>
    <ul class="price-col col-c row-deals"><h3>3 bundle deals</h3>
      <li>10, 12, 14 - $223</li><li>12, 14, 16 - $239</li><li>14, 16, 18 - $252</li><li>16, 18, 20 - $264</li><li>18, 20, 22 - $278</li><li>20, 22, 24 - $293</li><li>22, 24, 26 - $308</li><li>24, 26, 28 - $322</li><li>26, 28, 30 - $337</li><li>28, 30, 32 - $350</li><li>30, 32, 34 - $262</li><li>32, 34, 36 - $375</li><li>34, 36, 38 - $390</li>
    </ul>
    <ul class="price-col col-d row-deals"><h3>4 bundle deals</h3>
      <li>10, 12, 14, 16 - $293</li><li>12, 14, 16, 18 - $314</li><li>14, 16, 18, 20 - $325</li><li>16, 18, 20, 22 - $348</li><li>18, 20, 22, 24 - $367</li><li>20, 22, 24, 26 - $386</li><li>22, 24, 26, 28 - $407</li><li>24, 26, 28, 30 - $425</li><li>26, 28, 30, 32 - $444</li><li>28, 30, 32, 34 - $461</li><li>30, 32, 34, 36 - $477</li><li>32, 34, 36, 38 - $495</li>
    </ul>
  </section>

  <section class="page page--care">
    <div class="care-copy care-intro">
      <h2>Hair Care</h2>
      <p>It's very important to take good care of your hair to keep using long time, below are some brief introduction<br>
      <b>IMPORTANT:</b> Treat 100% human hair extensions gently.<br>
      1. Wash and condition hair regularly, at maximum of 3 times a week. This will keep the moisture in from shampooing while at the same time not drying them out from over shampooing.<br>
      2. Combing hair gently before washing. Do not rub or twist hair.<br>
      3. Add mild shampoo to cool water or warm water about 35℃ (Please do not use hot water) and swish hair till clean. Rinse thoroughly.<br>
      4. Blot out excess water with towel and allow hair to dry naturally. Do not expose to sun<br>
      5. Comb curly hair gently with your fingers from end to top. Do not brush<br>
      6. Hair may be tangled if general care directions are not followed properly.</p>
    </div>

    <div class="care-copy care-note">
      <h3>Important Note:</h3>
      <p>Brush the end of hair first, then the middle, and the top at last. DO NOT brush directly from the top and pull hard, it will break the hair. Regular care will keep the hair in good condition and avoid tangle problem, improper dyeing or other chemical process will damage the hair and cause tangle and shedding problem. Please wash the hair with warm water before proceeding dyeing.</p>
    </div>

    <div class="care-copy care-tips">
      <h3>Details of Hair Extension Maintenance Tips<br>Straight Hair:</h3>
      <p>Maintenance</p>
      <ul>
        <li>Shampoo at least once a week.</li>
        <li>Use a shampoo no higher than pH 7.</li>
        <li>Dilute one ounce of shampoo in a bowl or jug with a pint of warm water.</li>
        <li>Sponge the shampoo into the hair.</li>
        <li>Do not massage.</li>
        <li>Rinse thoroughly.</li>
        <li>Apply conditioner and comb hair, starting with the ends working your way up to your scalp.</li>
        <li>Rinse thoroughly.</li>
        <li>Let air-dry.</li>
      </ul>
    </div>

    <div class="care-copy care-daily">
      <h3>Daily</h3>
      <ul>
        <li>Brush or comb through to style.</li>
        <li>Use styling aids, such as mouse, gel, and hairspray in moderation (preferably alcohol free products).</li>
      </ul>
    </div>

    <div class="care-copy care-sleep">
      <h3>Sleep</h3>
      <ul>
        <li>Before going to bed, braid your hair into one loose large braid at the back of the neck.</li>
        <li>After waking up, undo braid and comb through beginning at the ends and working your way up to roots.</li>
      </ul>
    </div>

    <div class="swatch swatch--loose"><div class="swatch__fill" role="img" aria-label="Photo of loose wave hair bundles"></div></div>
    <div class="swatch swatch--body"><div class="swatch__fill" role="img" aria-label="Photo of body wave hair bundles"></div></div>
    <div class="swatch swatch--deep"><div class="swatch__fill" role="img" aria-label="Photo of deep wave hair bundles"></div></div>
    <div class="swatch swatch--straight"><div class="swatch__fill" role="img" aria-label="Photo of straight hair bundles"></div></div>
  </section>

  <span class="page-label page-label--2">page 2</span>
  <span class="page-label page-label--3">Page 3</span>
</div>
</body>
</html>
```